Workshop PPT Update for AI Transformation Sessions

Our strategic consulting firm runs strategy workshops using slides as workshop exercises. These slides are used to communicate to the participants in advance, run the workshops and produce the final deliverable.

It is time for a design "upgrade". We'd like them to be more engaging, hipper and more interesting. These slides are utilitarian, so clean and usable is good. I have attached the example of what we have today. I have also attached an example of another company's slides that I like.

We can't rip off their design nor can we go away 100% from what we have. But I think it is possible to "update" our look to something closer to their look. Grey colors are fine with some color pop.

Slide styles needed are - 1) Cover Page, 2) Instructions Page, 3) Bullet list 4) Worksheet (place for participants to add content 5) Table, 6) Two column.

```html
<!DOCTYPE html>
<html lang="en">
<head>
<meta charset="utf-8">
<title>Kickoff &amp; Discovery – Workshop Slides</title>
<link rel="stylesheet" href="https://fonts.googleapis.com/css2?family=Open+Sans:wght@400;600;700;800&display=swap">
<style>
:root{
  --canvas:#ececec;
  --paper:#ffffff;
  --ink:#2f323a;
  --muted:#6b6e76;
  --slate:#434752;
  --slate-deep:#3a3d47;
  --accent:#a83a35;
  --rule:#d9dadd;
  --row:#f1f1f2;
  --row-alt:#e4e5e7;
}
*{box-sizing:border-box;margin:0;padding:0}
html,body{width:1200px;height:3868px;overflow:hidden}
body{background:var(--canvas);font-family:"Open Sans",Arial,sans-serif;color:var(--ink);position:relative}
.slide{position:absolute;left:96px;width:1008px;height:567px;background:var(--paper);overflow:hidden;box-shadow:0 1px 4px rgba(0,0,0,.08)}
.slide--dark{background:var(--slate-deep);color:#fff}
.brand{position:absolute;top:22px;right:34px;text-align:right;line-height:1}
.brand__name{font-weight:700;font-size:21px;color:var(--ink);display:flex;align-items:center;gap:6px}
.brand__name::before{content:"";width:9px;height:9px;border-radius:50%;background:var(--accent)}
.brand__sub{display:block;font-size:8px;color:var(--muted);margin-top:3px}
.title-mark{position:absolute;left:0;top:26px;width:0;height:0;border-top:20px solid transparent;border-bottom:20px solid transparent;border-left:22px solid var(--accent)}
.title{position:absolute;left:44px;top:26px;font-size:31px;font-weight:800;line-height:40px;color:var(--ink)}
.title em{font-style:normal;color:var(--accent)}
.footer{position:absolute;left:40px;right:40px;bottom:20px;display:flex;justify-content:space-between;font-size:11px;font-weight:700;color:var(--ink)}
.slide--dark .footer{color:#fff}

/* Getting started */
.checklist{position:absolute;left:44px;top:96px;list-style:none}
.checklist li{display:flex;align-items:center;gap:12px;font-weight:700;font-size:15px;height:48px}
.checklist svg{flex:none}
.accent-band{position:absolute;left:360px;top:338px;width:220px;height:112px;background:var(--accent)}
.photo{position:absolute;left:560px;top:50px;width:370px;height:366px;background:linear-gradient(135deg,#d8d3cc,#a7a39e 55%,#6f6c6a)}

/* Cover */
.cover{position:absolute;inset:0;display:flex;flex-direction:column;align-items:center;justify-content:center;text-align:center}
.cover__brand{display:flex;align-items:center;gap:7px;font-weight:700;font-size:20px;margin-bottom:16px}
.cover__brand::before{content:"";width:9px;height:9px;border-radius:50%;background:var(--accent)}
.cover__title{font-size:40px;font-weight:800}
.cover__sub{font-size:13px;font-weight:600;margin-top:6px;color:#e2e3e6}

/* Panels */
.panel{position:absolute;background:var(--slate);color:#fff;border-radius:10px;text-align:center}
.panel__lead{font-size:17px;font-weight:600;margin-top:46px}
.panel__label{color:#e0655e;font-weight:700;font-size:14px;margin-top:34px}
.panel__list{list-style:none;font-size:15px;font-weight:600}
.panel__list li{margin-top:16px}

.flow{position:absolute;left:560px;top:96px;width:400px}
.flow__head{font-size:18px;font-weight:600;margin-bottom:12px}
.flow__item{display:flex;gap:8px;margin-bottom:11px}
.flow__item svg{flex:none;margin-top:2px}
.flow__name{font-size:12.5px;font-weight:700}
.flow__desc{font-size:9px;color:var(--muted);margin-top:1px}
.flow__deliv{color:var(--accent);font-weight:700;font-size:12.5px;margin-top:6px}
.flow__deliv-text{font-size:11px;margin-top:3px}

/* Instructions */
.purpose{position:absolute;left:44px;top:80px;font-size:12px}
.purpose b{font-weight:700}
.steps{position:absolute;left:44px;top:112px;width:420px}
.steps__label{color:var(--accent);font-weight:700;font-size:11px;margin-bottom:10px}
.step{display:flex;gap:8px;margin-bottom:16px}
.step svg{flex:none;margin-top:1px}
.step__name{font-size:12.5px;font-weight:700}
.step__desc{font-size:8.5px;color:var(--muted);margin-top:1px}

/* Table */
.plan{position:absolute;left:44px;top:100px;width:920px;border-collapse:collapse;font-size:12px}
.plan th{background:var(--slate);color:#fff;font-size:9px;font-weight:700;letter-spacing:.02em;height:26px;text-align:center}
.plan td{height:82px;text-align:center;vertical-align:middle;border-bottom:1px solid var(--paper)}
.plan tr:nth-child(odd) td{background:var(--row)}
.plan tr:nth-child(even) td{background:var(--row-alt)}
.plan .lvl{width:56px;font-size:10px;color:var(--muted)}
.plan .what{width:90px;font-size:11px}
.plan .what small{display:block;font-size:9px;color:var(--muted)}
.plan .elem{font-weight:700;font-size:12.5px}
.plan .elem small{display:block;font-weight:400;font-size:9px;color:var(--muted)}

/* Principles */
.question{position:absolute;left:44px;top:78px;font-size:15px;font-weight:700}
.principles{position:absolute;left:44px;top:112px;width:920px}
.principle{margin-bottom:16px}
.principle__name{display:flex;align-items:center;gap:8px;color:var(--accent);font-weight:800;font-size:16px}
.principle__desc{font-size:10.5px;font-weight:600;margin-top:5px;padding-left:4px}
</style>
</head>
<body>

<!-- Slide 02: Getting Started -->
<section class="slide" style="top:32px">
  <div class="title-mark"></div>
  <h1 class="title"><em>Getting</em> Started</h1>
  <div class="brand"><span class="brand__name">Northpath</span><span class="brand__sub">Consulting</span></div>
  <ul class="checklist">
    <li><svg width="18" height="18" viewBox="0 0 18 18"><circle cx="9" cy="9" r="8" fill="none" stroke="var(--accent)" stroke-width="2"/><path d="M5 9.5l3 3 5-6" fill="none" stroke="var(--accent)" stroke-width="2"/></svg>Complete the Engagement Sizing Survey.</li>
    <li><svg width="18" height="18" viewBox="0 0 18 18"><circle cx="9" cy="9" r="8" fill="none" stroke="var(--accent)" stroke-width="2"/><path d="M5 9.5l3 3 5-6" fill="none" stroke="var(--accent)" stroke-width="2"/></svg>Collect relevant inputs.</li>
    <li><svg width="18" height="18" viewBox="0 0 18 18"><circle cx="9" cy="9" r="8" fill="none" stroke="var(--accent)" stroke-width="2"/><path d="M5 9.5l3 3 5-6" fill="none" stroke="var(--accent)" stroke-width="2"/></svg>Determine workshop participants &amp; date.</li>
    <li><svg width="18" height="18" viewBox="0 0 18 18"><circle cx="9" cy="9" r="8" fill="none" stroke="var(--accent)" stroke-width="2"/><path d="M5 9.5l3 3 5-6" fill="none" stroke="var(--accent)" stroke-width="2"/></svg>Send invites, to include pre-work.</li>
  </ul>
  <div class="accent-band"></div>
  <div class="photo" role="img" aria-label="Photo of a team collaborating in a bright office"></div>
  <div class="footer"><span>22 Jan 2024</span><span>02</span></div>
</section>

<!-- Slide 03: Cover -->
<section class="slide slide--dark" style="top:680px">
  <div class="cover">
    <div class="cover__brand">Northpath</div>
    <h1 class="cover__title">Kickoff &amp; Discovery</h1>
    <p class="cover__sub">Sizing &amp; Scoping AI Transformation</p>
  </div>
  <div class="footer"><span>22 Jan 2024</span><span>03</span></div>
</section>

<!-- Slide 03: Workshop Overview -->
<section class="slide" style="top:1328px">
  <div class="title-mark"></div>
  <h1 class="title"><em>Workshop</em> Overview</h1>
  <div class="brand"><span class="brand__name">Northpath</span><span class="brand__sub">Consulting</span></div>
  <div class="panel" style="left:44px;top:100px;width:470px;height:390px">
    <p class="panel__lead">Participants: Execs; Duration: 2 hrs.</p>
    <p class="panel__label">Pre-Work</p>
    <ul class="panel__list">
      <li>Org Strategy</li>
      <li>2023 Goal Performance</li>
      <li>Existing policies</li>
      <li>Pre-thinking questions</li>
    </ul>
  </div>
  <div class="flow">
    <p class="flow__head">Workshop Flow</p>
    <div class="flow__item"><svg width="13" height="13" viewBox="0 0 14 14"><circle cx="7" cy="7" r="5.5" fill="none" stroke="var(--accent)" stroke-width="2"/></svg><div><p class="flow__name">Confirm Company Direction</p><p class="flow__desc">Review organization direction, vision and strategy.</p></div></div>
    <div class="flow__item"><svg width="13" height="13" viewBox="0 0 14 14"><circle cx="7" cy="7" r="5.5" fill="none" stroke="var(--accent)" stroke-width="2"/></svg><div><p class="flow__name">Develop AI Vision</p></div></div>
    <div class="flow__item"><svg width="13" height="13" viewBox="0 0 14 14"><circle cx="7" cy="7" r="5.5" fill="none" stroke="var(--accent)" stroke-width="2"/></svg><div><p class="flow__name">Develop AI Guiding Principles</p><p class="flow__desc">Draft guiding principles and supporting policy needs.</p></div></div>
    <div class="flow__item"><svg width="13" height="13" viewBox="0 0 14 14"><circle cx="7" cy="7" r="5.5" fill="none" stroke="var(--accent)" stroke-width="2"/></svg><div><p class="flow__name">Agree on a Governance Approach</p><p class="flow__desc">Agree governance model, roles and decision rights.</p></div></div>
    <div class="flow__item"><svg width="13" height="13" viewBox="0 0 14 14"><circle cx="7" cy="7" r="5.5" fill="none" stroke="var(--accent)" stroke-width="2"/></svg><div><p class="flow__name">Agree on a Training &amp; Learning Approach</p><p class="flow__desc">Plan approach to training and upskilling.</p></div></div>
    <div class="flow__item"><svg width="13" height="13" viewBox="0 0 14 14"><circle cx="7" cy="7" r="5.5" fill="none" stroke="var(--accent)" stroke-width="2"/></svg><div><p class="flow__name">Determine Rollout &amp; Communication</p><p class="flow__desc">Plan internal rollout and communication steps.</p></div></div>
    <p class="flow__deliv">Deliverable:</p>
    <p class="flow__deliv-text">Your Company's AI Playbook</p>
  </div>
  <div class="footer"><span>22 Jan 2024</span><span>03</span></div>
</section>

<!-- Slide 04: Instructions -->
<section class="slide" style="top:1976px">
  <div class="title-mark"></div>
  <h1 class="title"><em>Creating your</em> AI Guiding Principles</h1>
  <div class="brand"><span class="brand__name">Northpath</span><span class="brand__sub">Consulting</span></div>
  <p class="purpose"><b>Purpose:</b> To create behavioral statements that everyone is expected to adhere to.</p>
  <div class="steps">
    <p class="steps__label">INSTRUCTIONS:</p>
    <div class="step"><svg width="13" height="13" viewBox="0 0 14 14"><circle cx="7" cy="7" r="5.5" fill="none" stroke="var(--accent)" stroke-width="2"/></svg><div><p class="step__name">Create the Outline.</p><p class="step__desc">Determine key topics that need principles.</p></div></div>
    <div class="step"><svg width="13" height="13" viewBox="0 0 14 14"><circle cx="7" cy="7" r="5.5" fill="none" stroke="var(--accent)" stroke-width="2"/></svg><div><p class="step__name">Audit the Outline.</p><p class="step__desc">Check the list against existing policies and values.</p></div></div>
    <div class="step"><svg width="13" height="13" viewBox="0 0 14 14"><circle cx="7" cy="7" r="5.5" fill="none" stroke="var(--accent)" stroke-width="2"/></svg><div><p class="step__name">Draft the Guiding Principles.</p></div></div>
    <div class="step"><svg width="13" height="13" viewBox="0 0 14 14"><circle cx="7" cy="7" r="5.5" fill="none" stroke="var(--accent)" stroke-width="2"/></svg><div><p class="step__name">Determine which GPs need detailed policies.</p></div></div>
    <div class="step"><svg width="13" height="13" viewBox="0 0 14 14"><circle cx="7" cy="7" r="5.5" fill="none" stroke="var(--accent)" stroke-width="2"/></svg><div><p class="step__name">Determine which AI Tools support the GPs.</p></div></div>
    <div class="step"><svg width="13" height="13" viewBox="0 0 14 14"><circle cx="7" cy="7" r="5.5" fill="none" stroke="var(--accent)" stroke-width="2"/></svg><div><p class="step__name">Finalize via a legal and executive review.</p></div></div>
  </div>
  <div class="panel" style="left:560px;top:112px;width:404px;height:300px">
    <p class="panel__label" style="margin-top:34px">Pre-Existing Materials</p>
    <ul class="panel__list">
      <li>Company Values</li>
      <li>Current Policies (GDPR, CCPA, etc.)</li>
      <li>Legal Guidance</li>
      <li>OTHER</li>
    </ul>
  </div>
  <div class="footer"><span>22 Jan 2024</span><span>04</span></div>
</section>

<!-- Slide 05: Table -->
<section class="slide" style="top:2624px">
  <div class="title-mark"></div>
  <h1 class="title"><em>Plan</em> Structure</h1>
  <div class="brand"><span class="brand__name">Northpath</span><span class="brand__sub">Consulting</span></div>
  <table class="plan">
    <thead><tr><th colspan="2">LEVEL</th><th>PLANNING ELEMENT DEFINITION</th><th>ACCOUNTABILITY OWNER</th><th>FREQUENCY OF MODIFICATION</th></tr></thead>
    <tbody>
      <tr><td class="lvl">1</td><td class="what">What<small>(overall)</small></td><td class="elem">Strategic Priorities</td><td>N/A</td><td>3+ years</td></tr>
      <tr><td class="lvl">1.1</td><td class="what">What<small>(this year)</small></td><td class="elem">Goals<small>Outcomes &amp; Strategies</small></td><td>Executive Leadership</td><td>1-3 years</td></tr>
      <tr><td class="lvl">1.1.1</td><td class="what" rowspan="2">How</td><td class="elem">Key Performance Indicators<br>and/or Initiatives</td><td></td><td>1 year<br><small>(or only if needed)</small></td></tr>
      <tr><td class="lvl">1.1.1.1</td><td class="elem">Action Items</td><td></td><td>Quarterly/Monthly</td></tr>
    </tbody>
  </table>
  <div class="footer"><span>22 Jan 2024</span><span>05</span></div>
</section>

<!-- Slide 06: Worksheet -->
<section class="slide" style="top:3272px">
  <div class="title-mark"></div>
  <h1 class="title"><em>AI Guiding</em> Principles</h1>
  <div class="brand"><span class="brand__name">Northpath</span><span class="brand__sub">Consulting</span></div>
  <p class="question">What guides our decision-making and approach?</p>
  <div class="principles">
    <div class="principle"><p class="principle__name"><svg width="14" height="14" viewBox="0 0 14 14"><circle cx="7" cy="7" r="5.5" fill="none" stroke="var(--accent)" stroke-width="2"/></svg>PRINCIPLE #1:</p><p class="principle__desc">Complete perspective from Executives, Directors, Managers &amp; Staff. Conduct competitive analysis and customer research (optional).</p></div>
    <div class="principle"><p class="principle__name"><svg width="14" height="14" viewBox="0 0 14 14"><circle cx="7" cy="7" r="5.5" fill="none" stroke="var(--accent)" stroke-width="2"/></svg>PRINCIPLE #2</p><p class="principle__desc">Complete perspective from Executives, Directors, Managers &amp; Staff. Conduct competitive analysis and customer research (optional).</p></div>
    <div class="principle"><p class="principle__name"><svg width="14" height="14" viewBox="0 0 14 14"><circle cx="7" cy="7" r="5.5" fill="none" stroke="var(--accent)" stroke-width="2"/></svg>PRINCIPLE #3</p><p class="principle__desc">Complete perspective from Executives, Directors, Managers &amp; Staff. Conduct competitive analysis and customer research (optional).</p></div>
    <div class="principle"><p class="principle__name"><svg width="14" height="14" viewBox="0 0 14 14"><circle cx="7" cy="7" r="5.5" fill="none" stroke="var(--accent)" stroke-width="2"/></svg>PRINCIPLE #4</p><p class="principle__desc">Complete perspective from Executives, Directors, Managers &amp; Staff. Conduct competitive analysis and customer research (optional).</p></div>
    <div class="principle"><p class="principle__name"><svg width="14" height="14" viewBox="0 0 14 14"><circle cx="7" cy="7" r="5.5" fill="none" stroke="var(--accent)" stroke-width="2"/></svg>PRINCIPLE #5</p><p class="principle__desc">Complete perspective from Executives, Directors, Managers &amp; Staff. Conduct competitive analysis and customer research (optional).</p></div>
  </div>
  <div class="footer"><span>22 Jan 2024</span><span>06</span></div>
</section>

</body>
</html>
```